Mara Fenwick Music EP Design Artwork

EP musical recording cover art work. Mara Fenwick is a new artist in the Pop, Country Pop, Pop Rock, Americana and Singer-songwriter genres. The name of the EP is "Quiet Harbor Lights", and her first single is being released on all streaming platforms globally June 1st. We are looking for a graphic design that has that Pop/rock female artist appeal. marafenwick.com and all social media outlets are marafenwickmusic (reference). Your art work will be seen globally and we will give a personal shout out on all her socials to the design we select as a single post. Her signature logo is attached for a color and style example. Please try to use the signature within the EP cover design, but feel free to change the purple backing accordingly if another color is needed to fit better with the color scheme of your design.

Requirements
Must have
• Mara Fenwick signature logo and EP name

Some of you asked for hi res pics, use this link:

https://files.sharevault-example.net/folders/8kTr2WqLp4ZxNc7VbHd3MfYs1JaGe9Ro
Should not have
• June 1 on the EP art work. June 1 is the release of the first single on the EP. This is an album cover, we want it to look like a really cool pop female artist album cover, thanks.

```html
<!DOCTYPE html>
<html lang="en">
<head>
<meta charset="utf-8">
<title>Mara Fenwick — Quiet Harbor Lights</title>
<link rel="stylesheet" href="https://fonts.googleapis.com/css2?family=Roboto+Slab:wght@700;800&display=swap">
<style>
  :root {
    --paper: #efe4c6;
    --paper-dark: #e2d3ad;
    --frame: #111111;
    --amber: #d9961c;
    --amber-deep: #c98513;
    --stripe: #e6bb22;
    --splash: #f3e6c4;
    --title-blue: #3e5b77;
    --name-white: #ffffff;
  }
  html, body {
    margin: 0;
    padding: 0;
    width: 1200px;
    height: 1200px;
    overflow: hidden;
    background: var(--paper);
  }
  .cover {
    position: relative;
    width: 1200px;
    height: 1200px;
    background: radial-gradient(circle at 50% 50%, var(--paper) 60%, var(--paper-dark) 100%);
  }
  .cover__art {
    position: absolute;
    inset: 0;
  }
  .cover__photo {
    position: absolute;
    left: 270px;
    top: 290px;
    width: 600px;
    height: 840px;
    border-radius: 280px 280px 40px 40px;
    background: linear-gradient(180deg, #e9c9a0 0%, #2f3b44 38%, #cdb796 62%, #c9b392 88%, #1d1d1d 100%);
    opacity: 0.9;
  }
  .artist-name {
    position: absolute;
    left: 118px;
    top: 118px;
    margin: 0;
    font-family: "Roboto Slab", serif;
    font-weight: 700;
    font-size: 76px;
    line-height: 1;
    color: var(--name-white);
  }
  .ep-title {
    position: absolute;
    right: 118px;
    top: 930px;
    margin: 0;
    font-family: "Roboto Slab", serif;
    font-weight: 800;
    font-size: 80px;
    line-height: 0.98;
    text-align: right;
    color: var(--title-blue);
    letter-spacing: -1px;
  }
</style>
</head>
<body>
  <main class="cover">
    <svg class="cover__art" width="1200" height="1200" viewBox="0 0 1200 1200" aria-hidden="true">
      <defs>
        <radialGradient id="splashGlow" cx="0.5" cy="0.45" r="0.6">
          <stop offset="0" stop-color="var(--splash)"/>
          <stop offset="0.45" stop-color="#eed9a8"/>
          <stop offset="0.75" stop-color="var(--amber)"/>
          <stop offset="1" stop-color="var(--amber-deep)"/>
        </radialGradient>
      </defs>
      <rect class="frame-border" x="50" y="50" width="1100" height="1100" fill="var(--frame)"/>
      <rect class="frame-field" x="62" y="62" width="1076" height="1076" fill="url(#splashGlow)"/>
      <g class="accent-stripes" fill="var(--stripe)" opacity="0.85">
        <polygon points="680,210 1138,120 1138,170 680,260"/>
        <polygon points="760,290 1138,215 1138,240 760,315"/>
        <polygon points="62,360 330,330 330,370 62,400"/>
        <polygon points="62,420 300,395 300,410 62,435"/>
      </g>
    </svg>

    <div class="cover__photo" role="img" aria-label="Portrait photo of the artist crouching, wearing a dark denim jacket, beige trousers and black heeled boots"></div>

    <h1 class="artist-name">Mara Fenwick</h1>
    <h2 class="ep-title">QUIET HARBOR<br>LIGHTS</h2>
  </main>
</body>
</html>
```